Purchasing community for life science startups needs landing page for collecting of contact adresses

We are the "Pipette Union", the first purchasing community for life science startups. The idea is to bundle the needs of several smaller companies (laboratories) and to buy lab consumables and chemicals in larger quantities. This bargaining position, at the end of all participants can buy their products very low prices. In the attached powerpoint file you will find an idea and some elements, which demonstrate a little the style, which came into my mind.
Urlaub/Ferien
Target Market(s)
Our target customers are startups and smaller biotech companies, which are too small to get the best prices. The aim of this landing page is to collect all interested parties.
Look and feel

```html
<!DOCTYPE html>
<html lang="de">
<head>
<meta charset="utf-8">
<title>Pipette Union – Einkaufsgemeinschaft LifeScience</title>
<link href="https://fonts.googleapis.com/css2?family=Montserrat:wght@400;500;600;700&display=swap" rel="stylesheet">
<style>
  :root {
    --ink: #1d1d1f;
    --text: #2a2a2a;
    --accent: #17dce8;
    --accent-line: #23d3e3;
    --hero-bg: #eeeff1;
    --band-bg: #ffffff;
    --stripe-bg: #f5f5f5;
    --footer-bg: #eefafc;
    --input-border: #2fd5e4;
  }
  * { box-sizing: border-box; margin: 0; padding: 0; }
  html, body { width: 807px; height: 1200px; overflow: hidden; }
  body {
    position: relative;
    font-family: "Montserrat", sans-serif;
    color: var(--text);
    background: #fff;
  }
  .hero {
    position: absolute; left: 0; top: 0; width: 807px; height: 404px;
    text-align: center;
  }
  .hero-photo {
    position: absolute; inset: 0;
    background:
      radial-gradient(circle at 770px 170px, rgba(160,225,60,.55) 0, rgba(160,225,60,0) 90px),
      radial-gradient(circle at 640px 50px, rgba(215,240,90,.45) 0, rgba(215,240,90,0) 110px),
      radial-gradient(circle at 150px 90px, rgba(60,200,225,.35) 0, rgba(60,200,225,0) 110px),
      linear-gradient(180deg, #f3f4f6 0%, var(--hero-bg) 100%);
  }
  .hero-content { position: relative; }
  .brand { position: absolute; left: 0; width: 807px; top: 30px; display: flex; flex-direction: column; align-items: center; }
  .brand-mark { width: 34px; height: 34px; border-radius: 50%; background: var(--ink); margin-bottom: 10px; }
  .brand-name { font-size: 19px; font-weight: 600; letter-spacing: .3px; color: var(--ink); line-height: 1; }
  .brand-tag { font-size: 7.5px; color: var(--ink); margin-top: 2px; }
  .hero-title { position: absolute; left: 0; width: 807px; top: 167px; font-size: 13px; font-weight: 600; letter-spacing: .3px; color: var(--ink); }
  .hero-lead { position: absolute; left: 0; width: 807px; top: 201px; font-size: 11.2px; font-weight: 500; line-height: 14px; color: var(--ink); }
  .hero-offer { position: absolute; left: 0; width: 807px; top: 255px; font-size: 11.2px; font-weight: 600; line-height: 14px; color: var(--ink); }
  .cta {
    position: absolute; left: 203px; top: 300px; width: 403px; height: 46px;
    background: var(--accent); color: #fff; font-size: 11.5px; font-weight: 700;
    display: flex; align-items: center; justify-content: center; letter-spacing: .2px;
  }
  .benefits { position: absolute; left: 0; top: 404px; width: 807px; height: 67px; background: var(--band-bg); }
  .benefit { position: absolute; top: 16px; display: flex; align-items: center; gap: 10px; font-size: 9.8px; line-height: 12.5px; color: #444; letter-spacing: .2px; }
  .benefit svg { width: 36px; height: 36px; flex: none; }
  .about {
    position: absolute; left: 0; top: 471px; width: 807px; height: 285px;
    background: repeating-linear-gradient(135deg, #f7f7f7 0 2px, #f1f1f1 2px 4px);
    text-align: center;
  }
  .about-block { position: absolute; left: 0; width: 807px; }
  .about-heading { font-size: 10.2px; font-weight: 700; color: var(--ink); letter-spacing: .3px; }
  .about-heading::after { content: ""; display: block; width: 34px; height: 2px; background: var(--accent-line); margin: 5px auto 0; }
  .about-text { font-size: 9.8px; line-height: 12.5px; margin-top: 7px; color: #333; letter-spacing: .2px; }
  .signup { position: absolute; left: 0; top: 772px; width: 807px; text-align: center; }
  .signup-title { font-size: 11.5px; font-weight: 600; line-height: 14.5px; color: var(--ink); }
  .signup-text { font-size: 9.8px; line-height: 12.4px; margin-top: 10px; color: #333; letter-spacing: .2px; }
  .field {
    position: absolute; left: 231px; width: 346px; height: 34px;
    border: 1.5px solid var(--input-border); background: #fff;
    font: 400 10px "Montserrat", sans-serif; color: #555; padding-left: 10px;
    display: flex; align-items: center;
  }
  .submit {
    position: absolute; left: 231px; top: 1046px; width: 346px; height: 34px;
    background: var(--accent); color: #fff; font-size: 10.4px; font-weight: 700;
    display: flex; align-items: center; justify-content: center;
  }
  .footer { position: absolute; left: 0; top: 1102px; width: 807px; height: 98px; background: var(--footer-bg); font-size: 7.8px; color: #333; letter-spacing: .2px; }
  .footer-owner { position: absolute; left: 93px; top: 44px; }
  .footer-visual { position: absolute; left: 366px; top: 8px; width: 76px; height: 80px; background: linear-gradient(135deg, #c5a57a, #8e6d45); }
  .footer-links { position: absolute; left: 573px; top: 36px; width: 124px; text-align: center; line-height: 14px; }
</style>
</head>
<body>
  <header class="hero">
    <div class="hero-photo" role="img" aria-label="Laborfoto mit Reagenzgläsern, Erlenmeyerkolben, Mikrotiterplatte, Klemmbrett und Kugelschreiber"></div>
    <div class="hero-content">
      <div class="brand">
        <span class="brand-mark"></span>
        <span class="brand-name">PIPETTE UNION</span>
        <span class="brand-tag">Einkaufsgemeinschaft LifeScience</span>
      </div>
      <h1 class="hero-title">GEMEINSAM EINKAUFEN ZU GROẞHANDELSPREISEN</h1>
      <p class="hero-lead">Betreibst du ein LifeScience Labor?<br>Benötigst du regelmäßig Chemikalien, Laborglas und Verbrauchsmaterialien?<br>Sind deine Abnahmemengen zu klein, um maximale Rabatte zu erhalten?</p>
      <p class="hero-offer">Dann mach mit bei der ersten Pipette Union 2019 und<br>spare bis zu 40% im Einkauf.</p>
      <div class="cta">TRAGE DICH IN UNSERE INTERESSENTENLISTE EIN!</div>
    </div>
  </header>

  <section class="benefits">
    <div class="benefit" style="left:90px;">
      <svg viewBox="0 0 36 36"><circle cx="18" cy="18" r="17" fill="none" stroke="#333" stroke-width="1"/><text x="18" y="23" text-anchor="middle" font-family="Montserrat, sans-serif" font-size="14" fill="#333">%</text></svg>
      <span>Kaufe ein zu<br>Großhandelspreisen</span>
    </div>
    <div class="benefit" style="left:317px;">
      <svg viewBox="0 0 36 36"><circle cx="18" cy="18" r="17" fill="none" stroke="#333" stroke-width="1"/><ellipse cx="20" cy="15" rx="10" ry="6" fill="#333"/><ellipse cx="15" cy="20" rx="9" ry="5.5" fill="#555" stroke="#fff" stroke-width="1"/></svg>
      <span>Keine Verhandlungen<br>mit Lieferanten</span>
    </div>
    <div class="benefit" style="left:566px;">
      <svg viewBox="0 0 36 36"><circle cx="18" cy="18" r="17" fill="none" stroke="#333" stroke-width="1"/><rect x="10" y="9" width="16" height="18" fill="#555"/><line x1="9" y1="28" x2="27" y2="8" stroke="#fff" stroke-width="1.5"/></svg>
      <span>Keine Vertrags-<br>verpflichtung</span>
    </div>
  </section>

  <section class="about">
    <div class="about-block" style="top:16px;">
      <h2 class="about-heading">UNSER ZIEL</h2>
      <p class="about-text">ist der Aufbau der ersten Einkaufsgemeinschaft für LifeScience Labore,<br>über die jeder Teilnehmer seinen Laborbedarf zu Großhandelspreisen<br>decken kann.</p>
    </div>
    <div class="about-block" style="top:97px;">
      <h2 class="about-heading">DAS KAMPAGNENPRINZIP</h2>
      <p class="about-text">Wir bündeln euren Jahresbedarf an Chemikalien,<br>Verbrauchsmaterialien und Laborbedarf und treten den Herstellern<br>und Lieferanten gegenüber als ein starker Verhandlungspartner auf.<br>Je mehr Teilnehmer mitmachen, desto größer wird unsere<br>Verhandlungsmasse, desto besser unsere Einkaufspreise.</p>
    </div>
    <div class="about-block" style="top:203px;">
      <h2 class="about-heading">KEEP IT SIMPLE</h2>
      <p class="about-text">Wir verzichten auf Rahmenverträge, Mindestbestellmengen und<br>sonstigen Verpflichtungen! Gefällt euch der ausgehandelte Preis,<br>dann bezieht ihr ganz normal per Bestellung bei der<br>Pipette Union euren Bedarf.</p>
    </div>
  </section>

  <section class="signup">
    <h2 class="signup-title">Hast du Interesse an einer Teilnahme?<br>Dann trage dich gerne völlig unverbindlich in unsere Interessentenliste ein.</h2>
    <p class="signup-text">Um einen Eindruck von unseren Preisen zu erhalten schicken wir dir<br>eine vorläufige Preisliste zu und bitten dich um feedback.<br>Welche Artikel interessieren dich?<br>In welchen Mengen benötigst du diese?<br>Welche fehlen noch?</p>
  </section>

  <div class="field" style="top:890px;">email adress</div>
  <div class="field" style="top:942px;">last name</div>
  <div class="field" style="top:994px;">first name</div>
  <div class="submit">PREISLISTE PER EMAIL ERHALTEN</div>

  <footer class="footer">
    <span class="footer-owner">Einkaufsgemeinschaft Pipette Union e.K.</span>
    <div class="footer-visual" role="img" aria-label="Abbildung eines Versandkartons"></div>
    <div class="footer-links">IMPRESSUM<br>DATENSCHUTZERKLAERUNG</div>
  </footer>
</body>
</html>
```